Dalton Power Supply, Inc. Business Card Design

We are an Electrical Distributor looking for a Modern, Professional Business Card design.

Target Market(s)

Residential Commercial Industrial

Industry/Entity Type

Electrical

Contact Information for Business Card

Dalton Power Supply, Inc.
418 Maple Ridge Lane
Brookvale, NC 27514
555-214-7630
555-214-8842 Fax
daltonpower@brightmail-example.net

```html
<!DOCTYPE html>
<html lang="en">
<head>
<meta charset="utf-8">
<title>Dalton Power Supply, Inc. – Business Card</title>
<link href="https://fonts.googleapis.com/css2?family=Open+Sans:wght@600;700&display=swap" rel="stylesheet">
<style>
  :root {
    --bg: #e4e5e7;
    --card: #ffffff;
    --brown-dark: #7a4514;
    --brown-mid: #a8692c;
    --tan: #c08a4a;
    --orange: #f39a0b;
    --text: #4a2a12;
    --rule: #f0b451;
  }
  * { margin: 0; padding: 0; box-sizing: border-box; }
  html, body { width: 1200px; height: 800px; overflow: hidden; }
  body {
    background: var(--bg);
    font-family: "Open Sans", Arial, sans-serif;
    color: var(--text);
    position: relative;
  }
  .card {
    position: absolute;
    left: 250px; top: 200px;
    width: 700px; height: 400px;
    background: var(--card);
    box-shadow: 0 2px 6px rgba(0,0,0,.12);
    overflow: hidden;
  }
  .card__corner { position: absolute; left: 0; top: 0; }
  .brand {
    position: absolute;
    right: 48px; top: 140px;
    text-align: right;
    font-weight: 700;
    font-size: 40px;
    line-height: 1.05;
    letter-spacing: 2px;
    color: var(--orange);
    text-transform: uppercase;
  }
  .contact {
    position: absolute;
    right: 48px; top: 268px;
    width: 420px;
    font-weight: 600;
    font-size: 17px;
    line-height: 1.35;
  }
  .contact__row { display: flex; justify-content: space-between; }
  .contact__address { font-style: normal; }
  .contact__phones li { list-style: none; display: flex; align-items: center; gap: 6px; }
  .contact__icon { width: 16px; height: 16px; }
  .contact__rule { height: 1px; background: var(--rule); margin: 8px 0 6px; }
  .contact__email { text-align: right; }
</style>
</head>
<body>
  <div class="card">
    <svg class="card__corner" width="420" height="230" viewBox="0 0 420 230" role="img" aria-label="Decorative corner band in brown, tan and orange">
      <defs>
        <linearGradient id="cornerFill" x1="0" y1="0" x2="1" y2="1">
          <stop offset="0" stop-color="var(--brown-dark)"/>
          <stop offset="0.6" stop-color="var(--tan)"/>
          <stop offset="1" stop-color="var(--orange)"/>
        </linearGradient>
      </defs>
      <polygon points="0,0 420,0 0,225" fill="url(#cornerFill)"/>
    </svg>

    <div class="brand">Dalton Power<br>Supply, Inc.</div>

    <div class="contact">
      <div class="contact__row">
        <address class="contact__address">
          418 Maple Ridge Lane<br>
          Brookvale, NC 27514
        </address>
        <ul class="contact__phones">
          <li>
            <svg class="contact__icon" viewBox="0 0 16 16" aria-label="Phone">
              <circle cx="8" cy="8" r="8" fill="var(--brown-mid)"/>
              <path d="M5 4.5c0 4 2.5 6.8 6.5 7l.7-1.6-1.8-.9-.8.8c-1.3-.6-2.300-1.6-2.9-2.9l.8-.8-.9-1.8z" fill="#fff"/>
            </svg>
            555-214-7630
          </li>
          <li>
            <svg class="contact__icon" viewBox="0 0 16 16" aria-label="Fax">
              <circle cx="8" cy="8" r="8" fill="var(--brown-mid)"/>
              <rect x="5.5" y="3.8" width="5" height="3" fill="#fff"/>
              <rect x="4" y="7" width="8" height="4" rx="1" fill="#fff"/>
              <rect x="5.5" y="10" width="5" height="2.4" fill="#fff"/>
            </svg>
            555-214-8842
          </li>
        </ul>
      </div>
      <div class="contact__rule"></div>
      <div class="contact__email">daltonpower@brightmail-example.net</div>
    </div>
  </div>
</body>
</html>
```